New IPv6 service needs a Web Design

We're launching a brand new service which is designed to connect the current Internet Protocol (IPv4) to the new Internet Protocol (IPv6).
The logo can be found at http://www.lumaport.example
We're looking for a clean and simple design, nothing super-fancy. There has to be room for some menu items and a place where people can login (so an e-mail and password box and login button, which must be replaced by the username and a logout button when the user is logged in).
We need a place for a rotating billboard (see http://vq.example for an example) or a video.
Designs that incorporate IPv4 - IPv6 elements (images with interconnecting networks, videos doing the same) will be rated higher, although the basic design is still the primary concern.
We need :
- A main page, with the rotating billboard and some other typical main page stuff
- 2 subpages with different formatted content blocks (1 column and 2 column)
This is a very short design contest, since we intend to go live very soon. Decision will be made quickly.
PSD file is sufficient, but it must be easy to slice to HTML/CSS (but we'll do that part ourselves).
Target Market(s)
IT Professionals
Industry/Entity Type
Internet
Look and feel
Each slider illustrates characteristics of the customer's brand and the style your logo design should communicate.

```html
<!DOCTYPE html>
<html lang="en">
<head>
<meta charset="utf-8">
<title>Lumaport – IPv6 Connectivity</title>
<link rel="stylesheet" href="https://fonts.googleapis.com/css2?family=Source+Sans+3:wght@400;600;700&display=swap">
<style>
:root{
  --bar:#3b3b3b;
  --blue:#1a74b8;
  --blue-dark:#0d5a94;
  --blue-title:#1f6aa6;
  --red:#d9232e;
  --red-text:#c8262d;
  --ink:#333;
  --muted:#555;
  --line:#dcdcdc;
  --footer:#2a2a2a;
  --footer-text:#cfcfcf;
}
*{margin:0;padding:0;box-sizing:border-box}
html,body{width:873px;height:1200px;overflow:hidden;background:#fff}
body{position:relative;font-family:"Source Sans 3",Arial,sans-serif;color:var(--ink)}
.abs{position:absolute}

/* top bar */
.topbar{left:0;top:0;width:873px;height:35px;background:linear-gradient(#474747,#333)}
.search{left:444px;top:8px;width:159px;height:19px;border-radius:4px;background:linear-gradient(#fff,#e6e6e6);border:1px solid #bbb;font-size:10px;font-style:italic;color:#999;padding:2px 7px}
.search svg{position:absolute;right:6px;top:2px}
.welcome{left:646px;top:9px;font-size:13px;color:#eee}
.logout{left:730px;top:8px;width:48px;height:19px;background:var(--red);border-radius:3px;color:#fff;font-size:11px;font-weight:700;text-align:center;line-height:19px}

/* header */
.header{left:0;top:35px;width:873px;height:85px;background:linear-gradient(#fff,#ececec)}
.brand{left:104px;top:62px;font-size:40px;font-weight:700;color:var(--blue-dark);letter-spacing:-1px;line-height:1}
.login-title{left:490px;top:46px;font-size:13px;color:var(--blue-title)}
.field{top:66px;width:139px;height:20px;border:1px solid #bbb;border-radius:4px;background:linear-gradient(#f3f3f3,#fff);font-size:10px;font-style:italic;color:#888;padding:3px 8px}
.btn-login{left:730px;top:92px;width:48px;height:16px;background:#2e2e2e;color:#fff;font-size:10px;font-weight:600;text-align:center;line-height:16px;border-radius:2px}

/* nav */
.nav{left:95px;top:120px;width:683px;height:36px;background:linear-gradient(#2184c8,#0f63a3);display:flex;box-shadow:0 2px 3px rgba(0,0,0,.2)}
.nav a{color:#fff;text-decoration:none;font-size:11px;line-height:36px;text-align:center;border-right:1px solid rgba(255,255,255,.2)}
.nav a:last-child{border-right:0}

/* hero */
.hero{left:0;top:156px;width:873px;height:312px;background:linear-gradient(#fff,#ededed)}
.hero-art{left:96px;top:173px;width:442px;height:283px;background:radial-gradient(ellipse at 40% 45%,#5b82c9 0,#9fb3d8 30%,#e5e8ee 65%,#f4f4f4 100%);border-radius:8px}
.hero-title{left:518px;top:262px;font-size:26px;color:var(--red-text);font-weight:400}
.hero-text{left:520px;top:296px;width:250px;font-size:13px;line-height:20px;color:var(--muted)}
.btn-more{left:520px;top:373px;width:59px;height:28px;background:linear-gradient(#555,#222);border-radius:3px;color:#fff;font-size:14px;text-align:center;line-height:28px}
.arrows{left:721px;top:418px}

/* news */
.news{left:95px;top:496px;width:217px;height:284px;border:1px solid #ccc;background:#f6f6f6}
.tabs{left:8px;top:9px;width:199px;height:25px;border:1px solid #bbb;border-radius:13px;background:linear-gradient(#fafafa,#e4e4e4);display:flex;overflow:hidden}
.tabs span{flex:1;font-size:13px;text-align:center;line-height:24px;color:#444}
.tabs .active{background:linear-gradient(#2385c9,#0e5f9d);color:#fff;border-radius:13px}
.news-item{position:absolute;left:9px;width:200px;border-bottom:1px solid #e2e2e2;padding-bottom:8px}
.news-date{font-size:11px;font-weight:700;color:var(--red-text)}
.news-text{font-size:9px;line-height:13px;color:#333;margin-top:2px}
.read-all{font-size:11px;font-weight:600;color:var(--blue-title)}

.newsletter{left:95px;top:798px;width:217px;height:100px;background:var(--blue);border:3px solid #e5e5e5;border-radius:3px}
.newsletter h3{position:absolute;left:9px;top:7px;font-size:15px;font-weight:400;color:#fff}
.email{left:9px;top:36px;width:192px;height:20px;background:#fff;border-radius:4px;font-size:10px;font-style:italic;color:#777;padding:3px 8px}
.subscribe{left:135px;top:67px;width:68px;height:17px;background:var(--red);color:#fff;font-size:10px;font-weight:700;text-align:center;line-height:17px;border-radius:2px}

/* services */
.section-title{font-size:19px;font-weight:400;color:var(--blue-title)}
.card{width:208px;height:89px;border:1px solid #e2e2e2;border-radius:3px;background:linear-gradient(#fff,#f2f2f2);box-shadow:0 2px 3px rgba(0,0,0,.08)}
.card .icon{position:absolute;left:9px;top:10px}
.card h4{position:absolute;left:55px;top:8px;font-size:12px;font-weight:600;color:#333}
.card p{position:absolute;left:55px;top:25px;width:146px;font-size:9.5px;line-height:13px;color:#555}
.divider{left:326px;top:745px;width:452px;height:1px;background:var(--line)}
.team-photo{left:348px;top:799px;width:113px;height:96px;border-radius:4px;background:linear-gradient(135deg,#7e8895,#3a3f48 55%,#c9c3bf)}
.about-text{left:475px;top:796px;width:303px;font-size:9.5px;line-height:14.6px;color:#444}

/* footer */
.footer{left:0;top:925px;width:873px;height:275px;background:var(--footer)}
.f-title{font-size:15px;color:#fff;font-weight:400}
.f-list{list-style:none;font-size:9.5px;color:var(--footer-text)}
.f-list li{height:23px}
.social li{display:flex;align-items:center;gap:13px;height:28px}
.social i{display:block;width:11px;height:11px;border-radius:2px}
.contact{font-size:9.5px;color:var(--footer-text);line-height:18px}
.contact .brand-red{color:var(--red);font-size:13px;font-weight:700;line-height:18px}
.contact .row{display:flex}
.contact .row span:first-child{width:80px}
.map{left:588px;top:965px;width:190px;height:147px;border:2px solid #ddd;background:linear-gradient(135deg,#efe7cf,#e3dcc8 50%,#d9d5c6)}
.map-link{left:713px;top:1118px;font-size:9px;color:#e89a2e}
.f-brand{left:95px;top:1109px;font-size:36px;font-weight:700;color:#8a8a8a;letter-spacing:-1px;line-height:1}
.copy{left:95px;top:1160px;font-size:9px;line-height:12px;color:#bbb}
</style>
</head>
<body>

<div class="abs topbar"></div>
<div class="abs search">Search
  <svg width="15" height="13" viewBox="0 0 15 13"><circle cx="6" cy="5.5" r="4" fill="none" stroke="#555" stroke-width="1.6"/><line x1="9" y1="8.5" x2="13.5" y2="12" stroke="#555" stroke-width="2"/></svg>
</div>
<div class="abs welcome">Welcome User</div>
<div class="abs logout">Logout</div>

<header class="abs header"></header>
<div class="abs brand">Lumaport</div>
<div class="abs login-title">Member Login</div>
<div class="abs field" style="left:490px">Username</div>
<div class="abs field" style="left:639px">Password</div>
<div class="abs btn-login">Log In</div>

<nav class="abs nav">
  <a href="#" style="width:79px">HOME</a>
  <a href="#" style="width:104px">WHO WE ARE</a>
  <a href="#" style="width:105px">WHAT WE DO</a>
  <a href="#" style="width:111px">CASE STUDIES</a>
  <a href="#" style="width:75px">CAREER</a>
  <a href="#" style="width:115px">NEWS &amp; EVENTS</a>
  <a href="#" style="width:94px">CONTACT</a>
</nav>

<section class="abs hero"></section>
<div class="abs hero-art" role="img" aria-label="Illustration of networked laptops linked together"></div>
<h1 class="abs hero-title">Lorem ipsum dolor sit</h1>
<p class="abs hero-text">Aliquam molestie, mi et imperdiet euis­mod, dui purus auctor tellus, et inter­dum lacus lectus et ante.</p>
<div class="abs btn-more">More</div>
<svg class="abs arrows" width="60" height="26" viewBox="0 0 60 26">
  <circle cx="12" cy="13" r="11.5" fill="#f4f4f4" stroke="#aaa"/><path d="M14 8 L9 13 L14 18" fill="none" stroke="#333" stroke-width="2.4"/>
  <circle cx="45" cy="13" r="11.5" fill="#f4f4f4" stroke="#aaa"/><path d="M43 8 L48 13 L43 18" fill="none" stroke="#333" stroke-width="2.4"/>
</svg>

<aside class="abs news">
  <div class="abs tabs"><span class="active">Latest News</span><span>Latest Events</span></div>
  <div class="news-item" style="top:44px"><div class="news-date">June 02, 2012</div><div class="news-text">Lorem ipsum dolor sit amet, consectetur adipi­scing elit. Fusce accumsan, elit a suscipit sagit­tis.........</div></div>
  <div class="news-item" style="top:116px"><div class="news-date">June 01, 2012</div><div class="news-text">Lorem ipsum dolor sit amet, consectetur adipi­scing elit. Fusce accumsan, elit a suscipit sagit­tis.........</div></div>
  <div class="news-item" style="top:188px;border-bottom:0"><div class="news-date">May 31, 2012</div><div class="news-text">Lorem ipsum dolor sit amet, consectetur adipi­scing elit. Fusce accumsan, elit a suscipit sagit­tis.........</div></div>
  <div class="abs read-all" style="left:158px;top:258px">Read All</div>
</aside>

<div class="abs newsletter">
  <h3>Newsletter Sign Up</h3>
  <div class="abs email">Enter Email Address</div>
  <div class="abs subscribe">Subscribe</div>
</div>

<h2 class="abs section-title" style="left:346px;top:490px">What We Do</h2>
<div class="abs card" style="left:346px;top:526px">
  <svg class="icon" width="36" height="36"><circle cx="18" cy="18" r="16" fill="#5a7fa3"/><circle cx="14" cy="13" r="7" fill="#a9c6e0" opacity=".7"/></svg>
  <h4>Application Development</h4><p>Aliquam molestie, mi et imperdiet euismod, dui purus auctor tellus, et interdum lacus lectus et ante.</p>
</div>
<div class="abs card" style="left:570px;top:526px">
  <svg class="icon" width="38" height="36"><rect x="2" y="6" width="18" height="13" fill="#2b55c4" stroke="#666"/><rect x="16" y="12" width="18" height="13" fill="#3a6ad8" stroke="#666"/><rect x="10" y="27" width="16" height="5" rx="2" fill="#3a9a3a"/></svg>
  <h4>Interconnecting Networks</h4><p>Aliquam molestie, mi et imperdiet euismod, dui purus auctor tellus, et interdum lacus lectus et ante.</p>
</div>
<div class="abs card" style="left:346px;top:636px">
  <svg class="icon" width="36" height="36"><circle cx="18" cy="18" r="16" fill="#49b336"/><path d="M10 15 A8 8 0 0 1 25 13 L28 10 L28 18 L20 18 L23 15 A5 5 0 0 0 13 16 Z M26 21 A8 8 0 0 1 11 23 L8 26 L8 18 L16 18 L13 21 A5 5 0 0 0 23 20 Z" fill="#fff"/></svg>
  <h4>Migration Solutions</h4><p>Aliquam molestie, mi et imperdiet euismod, dui purus auctor tellus, et interdum lacus lectus et ante.</p>
</div>
<div class="abs card" style="left:570px;top:636px">
  <svg class="icon" width="38" height="40"><rect x="2" y="18" width="14" height="11" fill="#2b6ad0" stroke="#777"/><circle cx="24" cy="13" r="11" fill="#1e6fd8"/><path d="M6 8 L14 8 L14 14" fill="none" stroke="#e08a1e" stroke-width="2"/></svg>
  <h4>Web Portal Development</h4><p>Aliquam molestie, mi et imperdiet euismod, dui purus auctor tellus, et interdum lacus lectus et ante.</p>
</div>

<div class="abs divider"></div>
<h2 class="abs section-title" style="left:346px;top:762px">Who We Are</h2>
<div class="abs team-photo" role="img" aria-label="Photo of the company team in business attire"></div>
<p class="abs about-text">Aliquam molestie, mi et imperdiet euismod, dui purus auctor tellus, et interdum lacus lectus et ante. Sed accumsan sollicitudin sapien, sit amet adipiscing turpis gravida ac. In congue, neque ac lobortis volutpat, libero mauris varius mi, vitae suscipit ipsum ligula vitae risus. Duis aliquam nibh a dui iaculis viverra id a velit. Vivamus egestas risus in magna varius commodo.</p>
<div class="abs read-all" style="left:732px;top:884px">Read All</div>

<footer class="abs footer"></footer>
<h3 class="abs f-title" style="left:95px;top:933px">Company</h3>
<ul class="abs f-list" style="left:95px;top:957px">
  <li>Home</li><li>Who We Are</li><li>What We Do</li><li>Case Studies</li><li>Career</li><li>News &amp; Events</li>
</ul>
<h3 class="abs f-title" style="left:237px;top:933px">Connect Us</h3>
<ul class="abs f-list social" style="left:237px;top:950px">
  <li><i style="background:#4aa6d8"></i>Chatter</li>
  <li><i style="background:#3b5a9a"></i>Friendbook</li>
  <li><i style="background:#2a77b0"></i>Linkwork</li>
  <li><i style="background:#777"></i>Circles +</li>
  <li><i style="background:#e07a1e"></i>Rss Feed</li>
</ul>
<h3 class="abs f-title" style="left:386px;top:933px">Contact Us</h3>
<div class="abs contact" style="left:386px;top:952px">
  <div class="brand-red">Lumaport</div>
  <div>1420 Kestrel Lane</div>
  <div>Harrowby, K12 4PL.</div>
  <div class="row"><span>Freephone:</span><span>+1 800 555 0142</span></div>
  <div class="row"><span>Telephone:</span><span>+1 955 555 0187</span></div>
  <div class="row"><span>FAX:</span><span>+1 105 555 0163</span></div>
  <div class="row"><span>E-mail:</span><span>info@lumaport.example</span></div>
</div>
<h3 class="abs f-title" style="left:588px;top:934px">Find our Location</h3>
<div class="abs map" role="img" aria-label="Street map showing the office location"></div>
<div class="abs map-link">Click for full Map</div>
<div class="abs f-brand">Lumaport</div>
<div class="abs copy">Copyright © 2012<br>All Right Reserved | Privacy Policy</div>

</body>
</html>
```